Business Card Design

I need a business card designed for my new company BrightOak Home developments I specialise in all aspects of carpentry including Decks, Pergolas, Conventional Framing and fit outs I am open to different colours as long as it fits with my logo.

Industry/Entity Type

Carpentry

Contact Information for Business Card

BrightOak Home Developments, Rob Keltmore, 0481604328, specialising in all aspects of carpentry and construction

```html
<!DOCTYPE html>
<html lang="en">
<head>
<meta charset="utf-8">
<title>BrightOak Home Developments – Business Card</title>
<link rel="stylesheet" href="https://fonts.googleapis.com/css2?family=Open+Sans:wght@400;600;700&display=swap">
<style>
  :root {
    --backdrop: #c9c9c9;
    --card-white: #f4f5f6;
    --card-shade: #e3e5e8;
    --brand-blue: #2f6cc4;
    --logo-blue: #3a5fb8;
    --title-blue: #3f74c9;
    --ink: #2b2b2b;
    --accent-magenta: #b52fc8;
    --back-navy: #2f3440;
    --back-navy-light: #3a404d;
    --tab-light: #e9eaec;
    --tab-ink: #3a3d44;
  }
  * { box-sizing: border-box; margin: 0; padding: 0; }
  html, body { width: 1200px; height: 894px; overflow: hidden; }
  body {
    background: var(--backdrop);
    font-family: "Open Sans", Arial, sans-serif;
    position: relative;
  }
  .card {
    position: absolute;
    width: 640px;
    height: 366px;
    left: 280px;
    border-radius: 4px;
    overflow: hidden;
    box-shadow: 0 6px 18px rgba(0,0,0,.18);
  }
  .card--front {
    top: 52px;
    background: radial-gradient(ellipse at 60% 55%, #ffffff 0%, var(--card-white) 45%, var(--card-shade) 100%);
  }
  .card--back {
    top: 474px;
    background: linear-gradient(135deg, var(--back-navy-light), var(--back-navy));
  }

  .brand {
    position: absolute;
    left: 150px;
    top: 62px;
    display: flex;
    align-items: center;
    gap: 12px;
  }
  .brand__mark {
    width: 34px; height: 34px;
    background: var(--logo-blue);
  }
  .brand__name {
    color: var(--logo-blue);
    font-weight: 600;
    font-size: 22px;
    letter-spacing: .5px;
    line-height: 1.1;
  }

  .holder {
    position: absolute;
    left: 40px;
    top: 164px;
    display: flex;
    align-items: baseline;
    gap: 10px;
  }
  .holder__name { color: var(--brand-blue); font-weight: 700; font-size: 27px; }
  .holder__divider { color: var(--brand-blue); font-weight: 400; font-size: 28px; }
  .holder__title { color: var(--title-blue); font-size: 17px; font-weight: 400; }

  .address {
    position: absolute;
    left: 40px;
    top: 210px;
    color: var(--ink);
    font-weight: 700;
    font-size: 16px;
    white-space: nowrap;
  }

  .contact-band {
    position: absolute;
    left: 0;
    top: 248px;
    width: 560px;
    height: 46px;
    background: var(--brand-blue);
    border-radius: 0 23px 23px 0;
    display: flex;
    align-items: center;
    gap: 22px;
    padding-left: 18px;
    list-style: none;
  }
  .contact-band__item {
    display: flex; align-items: center; gap: 8px;
    color: #fff; font-size: 15.5px; white-space: nowrap;
  }
  .contact-band__icon {
    width: 20px; height: 20px; border-radius: 50%;
    background: var(--accent-magenta);
    display: flex; align-items: center; justify-content: center;
  }

  .web-tab {
    position: absolute;
    left: 0;
    top: 38px;
    height: 44px;
    padding: 0 28px 0 22px;
    background: var(--tab-light);
    border-radius: 0 22px 22px 0;
    display: flex; align-items: center;
    color: var(--tab-ink);
    font-size: 18px;
    letter-spacing: 1.5px;
  }
</style>
</head>
<body>

  <section class="card card--front" aria-label="Business card front">
    <div class="brand">
      <span class="brand__mark" aria-hidden="true"></span>
      <span class="brand__name">BRIGHTOAK<br>HOME DEVELOPMENTS</span>
    </div>

    <div class="holder">
      <span class="holder__name">Rob Keltmore</span>
      <span class="holder__divider">|</span>
      <span class="holder__title">President &amp; Ceo</span>
    </div>

    <p class="address">Unit 7, 42 Timberline Court, Oakridge</p>

    <ul class="contact-band">
      <li class="contact-band__item">
        <span class="contact-band__icon">
          <svg width="11" height="11" viewBox="0 0 24 24"><path fill="#fff" d="M6.6 10.8a15.1 15.1 0 0 0 6.6 6.6l2.2-2.2a1 1 0 0 1 1-.25 11.4 11.4 0 0 0 3.6.57 1 1 0 0 1 1 1V20a1 1 0 0 1-1 1A17 17 0 0 1 3 4a1 1 0 0 1 1-1h3.5a1 1 0 0 1 1 1c0 1.25.2 2.45.57 3.570a1 1 0 0 1-.25 1z"/></svg>
        </span>0481 604 328
      </li>
      <li class="contact-band__item">
        <span class="contact-band__icon">
          <svg width="11" height="11" viewBox="0 0 24 24"><path fill="#fff" d="M6.6 10.8a15.1 15.1 0 0 0 6.6 6.6l2.2-2.2a1 1 0 0 1 1-.25 11.4 11.4 0 0 0 3.6.57 1 1 0 0 1 1 1V20a1 1 0 0 1-1 1A17 17 0 0 1 3 4a1 1 0 0 1 1-1h3.5a1 1 0 0 1 1 1c0 1.25.2 2.45.57 3.57a1 1 0 0 1-.25 1z"/></svg>
        </span>0481 604 328
      </li>
      <li class="contact-band__item">
        <span class="contact-band__icon">
          <svg width="11" height="11" viewBox="0 0 24 24"><path fill="#fff" d="M2 5h20v14H2zm2 2v.5l8 5 8-5V7l-8 5z"/></svg>
        </span>rob@brightoakhd.com
      </li>
    </ul>
  </section>

  <section class="card card--back" aria-label="Business card back">
    <div class="web-tab">www.brightoakhd.com</div>
  </section>

</body>
</html>
```